Beauty Packaging Design for small bottle

Design label to have a similar look and feel as other products (as attached for reference). This will be a printed on a gold metallic label, so although the design should be in gold to show us how it will eventually look, the final file will need to have the gold areas in red.

All project information is outline in the attached brief. Please contact us for any questions along the way.

Target Market(s)

Educated, savvy women 30-65 yrs old.

Industry/Entity Type

Hair And Beauty

Font styles to use
Other font styles liked:
• See brief

Requirements
Must have
• See brief
• Color(s): black, gold, white
Nice to have
• purple (CMYK 33/55/0/51)
Should not have
• See brief

```html
<!DOCTYPE html>
<html lang="en">
<head>
<meta charset="utf-8">
<title>Nightfall Plus – Bottle Label</title>
<link rel="stylesheet" href="https://fonts.googleapis.com/css2?family=Josefin+Sans:wght@300&family=Montserrat:wght@600&family=Quicksand:wght@500;600&family=Parisienne&display=swap">
<style>
  :root {
    --page: #ffffff;
    --label-black: #141214;
    --gold: #c9a552;
    --gold-frame: #bf9a48;
    --text-white: #f4f2f5;
    --text-soft: #dcd8de;
  }
  html, body {
    margin: 0;
    padding: 0;
    width: 1200px;
    height: 1200px;
    overflow: hidden;
    background: var(--page);
  }
  .canvas {
    position: relative;
    width: 1200px;
    height: 1200px;
  }
  .label {
    position: absolute;
    left: 230px;
    top: 80px;
    width: 740px;
    height: 1040px;
    background: var(--label-black);
  }
  .label__frame {
    position: absolute;
    left: 75px;
    top: 83px;
    width: 598px;
    height: 890px;
    border: 5px solid var(--gold-frame);
    box-sizing: border-box;
  }
  .brand {
    position: absolute;
    left: 82px;
    top: 0;
    display: flex;
    align-items: center;
  }
  .brand__mark {
    width: 135px;
    height: 150px;
    background: var(--gold);
  }
  .brand__name {
    margin-left: 30px;
    font-family: "Josefin Sans", sans-serif;
    font-weight: 300;
    font-size: 64px;
    letter-spacing: 6px;
    color: var(--gold);
    padding: 14px 0 8px;
    border-bottom: 2px solid var(--gold);
    line-height: 1;
  }
  .product {
    position: absolute;
    left: 82px;
    top: 300px;
  }
  .product__title {
    display: flex;
    align-items: baseline;
    margin: 0;
    white-space: nowrap;
  }
  .product__name {
    font-family: "Montserrat", sans-serif;
    font-weight: 600;
    font-size: 60px;
    color: var(--text-white);
    letter-spacing: -0.5px;
  }
  .product__plus {
    font-family: "Parisienne", cursive;
    font-size: 88px;
    color: var(--gold);
    margin-left: 6px;
    line-height: 0.8;
  }
  .product__tagline {
    margin: 10px 0 0 4px;
    font-family: "Quicksand", sans-serif;
    font-style: italic;
    font-weight: 500;
    font-size: 19px;
    color: var(--text-soft);
    border-bottom: 2px solid var(--gold);
    display: inline-block;
    padding-bottom: 6px;
    width: 330px;
  }
  .ingredients {
    position: absolute;
    left: 82px;
    top: 505px;
    margin: 0;
    padding: 0;
    list-style: none;
    font-family: "Quicksand", sans-serif;
    font-weight: 500;
    font-size: 32px;
    line-height: 50px;
    color: var(--text-white);
  }
  .ingredients li {
    position: relative;
    padding-left: 30px;
  }
  .ingredients li::before {
    content: "";
    position: absolute;
    left: 2px;
    top: 22px;
    width: 6px;
    height: 6px;
    border-radius: 50%;
    background: var(--text-soft);
  }
  .volume {
    position: absolute;
    left: 82px;
    top: 790px;
    font-family: "Quicksand", sans-serif;
    font-weight: 600;
    font-size: 36px;
    color: var(--gold);
    margin: 0;
  }
</style>
</head>
<body>
  <main class="canvas">
    <section class="label">
      <div class="label__frame">
        <div class="brand">
          <div class="brand__mark"></div>
          <span class="brand__name">LUMERA</span>
        </div>

        <div class="product">
          <h1 class="product__title">
            <span class="product__name">Nightfall</span>
            <span class="product__plus">Plus</span>
          </h1>
          <p class="product__tagline">Intensive Overnight Moisturizer</p>
        </div>

        <ul class="ingredients">
          <li>Retinol 2.5% Plus</li>
          <li>Hyaluronic Acid</li>
          <li>Aloe Vera, Sunflower Oil,<br>Jojoba Oil, Shea Butter</li>
          <li>Vitamin E &amp; Green Tea</li>
        </ul>

        <p class="volume">2 fl.oz | 60ml</p>
      </div>
    </section>
  </main>
</body>
</html>
```